Ronan Pike Building Business Card Design

Hi,

I need a business card for my Building company.
I am a Builder and build homes for clients.
I am looking for a sophisticated logo that can be used on business cards, envelopes and letter heads.
I am trying to take my business to the next level and need a professional business card.

Colours: Please use white, black, dark grey and bright blue.

Thank you,

Marnie and Ronan.

Target Market(s)

1. Home and Building Companies 2. Potential customers

Industry/Entity Type

Business

Contact Information for Business Card

Ronan Pike Building PTY LTD

Ronan Pike

Director

A.B.N. 37 902 518 617

BUILDERS LICENCE No. 573019k

Mobile: 0471 283 906

Email: ronanpikebuilding@maildrop-example.com.au

Requirements
Must have
• The following is compulsory to have in the designs:

Ronan Pike Building PTY LTD (business name)

Ronan Pike (contact name)

Director (position)

A.B.N. 37 902 518 617

Builders Licence No. 573019k

Mobile: 0471 283 906

Nice to have
• Logo for business
Should not have
• Should not be cluttered.

I am looking for a clean, sophisticated and professional business card design.

```html
<!DOCTYPE html>
<html lang="en">
<head>
<meta charset="utf-8">
<title>Ronan Pike Building – Business Card</title>
<link href="https://fonts.googleapis.com/css2?family=Tinos:wght@400;700&display=swap" rel="stylesheet">
<style>
  :root {
    --canvas: #ebebeb;
    --white: #ffffff;
    --ink: #1a1a1a;
    --bar: #231f20;
    --blue: #0a89c8;
    --rule: #9a9a9a;
    --shadow: rgba(30, 30, 30, 0.6);
  }
  * { margin: 0; padding: 0; box-sizing: border-box; }
  html, body {
    width: 994px; height: 1200px; overflow: hidden;
    background: var(--canvas);
    font-family: "Tinos", "Times New Roman", serif;
  }
  .card {
    position: absolute; left: 78px; width: 783px; height: 457px;
    box-shadow: 24px 30px 20px var(--shadow);
  }
  .card--front { top: 43px; background: var(--white); }
  .card--back { top: 620px; background: var(--blue); color: var(--white); }

  .rule {
    position: absolute; left: 14px; right: 14px; height: 2px;
    background: linear-gradient(90deg, transparent, var(--rule) 50%, transparent);
  }
  .card--back .rule {
    background: linear-gradient(90deg, transparent, rgba(255,255,255,.85) 50%, transparent);
  }
  .rule--top { top: 56px; }
  .rule--bottom { top: 399px; }

  .edge-bar {
    position: absolute; left: 0; top: 105px; width: 18px; height: 239px;
    background: var(--bar);
  }
  .brand-mark {
    position: absolute; display: flex; flex-direction: column;
    justify-content: center; align-items: center; text-align: center;
    font-weight: 400; line-height: 1.05;
  }
  .card--front .brand-mark {
    left: 40px; top: 125px; width: 216px; height: 205px;
    color: var(--blue); font-size: 46px;
  }
  .card--back .brand-mark {
    left: 520px; top: 90px; width: 250px; height: 270px;
    color: var(--white); font-size: 54px;
  }
  .divider {
    position: absolute; left: 277px; top: 119px; width: 1px; height: 226px;
    background: var(--rule);
  }
  .company-name {
    position: absolute; left: 350px; top: 118px;
    font-size: 37px; font-weight: 400; color: var(--ink); white-space: nowrap;
  }
  .company-name .accent { color: var(--blue); }
  .company-name .suffix { font-size: 8px; color: var(--blue); margin-left: 2px; }
  .credentials {
    position: absolute; left: 338px; top: 192px; width: 445px; height: 148px;
    background: var(--blue); color: var(--white);
    padding: 26px 0 0 17px; font-weight: 700; font-size: 25px; line-height: 1;
  }
  .credentials p + p { margin-top: 42px; }

  .person {
    position: absolute; left: 61px; top: 106px;
    font-weight: 700; font-size: 34px; line-height: 1.35;
  }
  .contact {
    position: absolute; left: 43px; top: 286px;
    font-weight: 700; font-size: 25px; white-space: nowrap;
  }
  .contact p + p { margin-top: 25px; }
</style>
</head>
<body>
  <section class="card card--front">
    <div class="rule rule--top"></div>
    <div class="edge-bar"></div>
    <div class="brand-mark"><span>Ronan</span><span>Pike</span></div>
    <div class="divider"></div>
    <h1 class="company-name">Ronan <span class="accent">Pike</span> Building<span class="suffix">PTY LTD</span></h1>
    <div class="credentials">
      <p>A.B.N. 37 902 518 617</p>
      <p>Builders Licence No. 573019k</p>
    </div>
    <div class="rule rule--bottom"></div>
  </section>

  <section class="card card--back">
    <div class="rule rule--top"></div>
    <div class="person">
      <p>Ronan Pike</p>
      <p>Director</p>
    </div>
    <div class="brand-mark"><span>Ronan</span><span>Pike</span></div>
    <div class="contact">
      <p>Mobile: 0471 283 906</p>
      <p>Email: ronanpikebuilding@maildrop-example.com.au</p>
    </div>
    <div class="rule rule--bottom"></div>
  </section>
</body>
</html>
```